Design of slide which will later be converted to video

We need slides which will be converted to a video format for web and social media marketing. We are attaching our concept draft as a start

All slides are provided as background only at this point, but if someone has a great idea for any of the other topics, feel free to provide that as well.

Using the attached slides (11-15), please re-create the slides in a more artistic and unified presentation, using stock images of the dog characters (no animation). The Professor must be a Basset hound with glasses; the other dog characters should be similar to the ones used in the slides. Voices and music will be added later. Any detail that can be added to make the video a seamless narrative is encouraged.
Original source files for pics here: tulvexcanine-my.sharepoint-example.com/:f:/p/rodney/Kq_T8WPLx4vHmRzaNcf-bYsDkVm7Xtgahwe3Lp19B4M0Qz?e=HUMBAR
Updates

We have updated our brief to include source files for our images. Many designers have asked for this. Please have a look!

Target Market(s)

Fresh Pet Food

Industry/Entity Type

Pet Food

Colors
EB3D1F
EC4F4E
F09395
F8D3D4
FCEDEE

Requirements
Must have
• We want to keep the picture of the basset hound with glasses. We can potentially use other pictures of the other dogs, but not necessary. All dogs must be real pictures, no animation! The chalkboard needs to be a chalkboard - do not change it to something else, but please feel free to improve its look. This improvement - to all of our graphics - is what we are looking for.
Nice to have
• The chalkboard text come in as being written in real time; the dog pictures selected can be changed as per the designder creative instincts. We are pretty committed to the Basset Hound playing Professor Wickersham, but we are always open to suggestion

```html
<!DOCTYPE html>
<html lang="en">
<head>
<meta charset="UTF-8">
<title>Slide 12 – Ask the Professor</title>
<link rel="stylesheet" href="https://fonts.googleapis.com/css2?family=Source+Sans+3:wght@400&display=swap">
<style>
  :root {
    --page: #ffffff;
    --bracket: #0c0c0c;
    --bubble-top: #3a6645;
    --bubble-mid: #2c5430;
    --bubble-tail: #1d4a26;
    --bubble-text: #ffffff;
    --label: #5a5a5a;
    --scene-leaf: #7f9a45;
    --scene-dark: #3f5038;
    --scene-sky: #c9d6dc;
    --dog-coat: #a59a8c;
    --dog-chest: #e4ddd6;
  }
  * { box-sizing: border-box; margin: 0; padding: 0; }
  html, body { width: 1200px; height: 1000px; overflow: hidden; background: var(--page); }
  .canvas { position: relative; width: 1200px; height: 1000px; font-family: "Source Sans 3", "Myriad Pro", sans-serif; }

  .slide { position: absolute; left: 50px; top: 135px; width: 1100px; height: 729px; overflow: hidden; }
  .slide__backdrop {
    position: absolute; inset: 0;
    background:
      radial-gradient(ellipse 30% 35% at 18% 30%, rgba(160,180,80,.75), transparent 70%),
      radial-gradient(ellipse 25% 30% at 80% 65%, rgba(225,235,240,.8), transparent 70%),
      radial-gradient(ellipse 30% 30% at 55% 60%, rgba(150,170,70,.7), transparent 70%),
      radial-gradient(ellipse 25% 25% at 85% 10%, rgba(240,245,248,.85), transparent 70%),
      radial-gradient(ellipse 35% 30% at 40% 95%, rgba(40,55,45,.8), transparent 70%),
      linear-gradient(135deg, var(--scene-leaf), var(--scene-dark) 55%, var(--scene-sky));
  }
  .slide__professor {
    position: absolute; left: 70px; top: 359px; width: 294px; height: 370px;
    border-radius: 48% 48% 6% 6% / 30% 30% 4% 4%;
    background: linear-gradient(180deg, var(--dog-coat) 0%, var(--dog-chest) 55%, var(--dog-coat) 100%);
  }

  .bracket { position: absolute; background: var(--bracket); }
  .bracket--tl-h { left: 50px;  top: 46px;  width: 233px; height: 8px; }
  .bracket--tl-v { left: 50px;  top: 46px;  width: 8px;   height: 181px; }
  .bracket--br-v { left: 1041px; top: 414px; width: 8px;  height: 405px; }
  .bracket--br-h { left: 665px; top: 676px; width: 384px; height: 8px; }

  .speech { position: absolute; left: 414px; top: 51px; width: 635px; height: 376px; }
  .speech svg { position: absolute; inset: 0; }
  .speech__text {
    position: absolute; left: 69px; top: 38px;
    color: var(--bubble-text); font-size: 51px; line-height: 73px; font-weight: 400;
    letter-spacing: 0.2px; white-space: nowrap;
  }

  .slide-label {
    position: absolute; left: 50px; top: 904px;
    font-size: 50px; line-height: 1; color: var(--label); font-weight: 400;
  }
</style>
</head>
<body>
<div class="canvas">
  <section class="slide">
    <div class="slide__backdrop" role="img" aria-label="Softly blurred green foliage and sky background"></div>
    <div class="slide__professor" role="img" aria-label="Photo of a brindle whippet-type dog wearing dark-rimmed glasses, looking at the viewer"></div>

    <span class="bracket bracket--tl-h"></span>
    <span class="bracket bracket--tl-v"></span>
    <span class="bracket bracket--br-v"></span>
    <span class="bracket bracket--br-h"></span>

    <div class="speech">
      <svg width="635" height="376" viewBox="0 0 635 376" aria-hidden="true">
        <defs>
          <linearGradient id="bubbleFill" x1="0" y1="0" x2="1" y2="1">
            <stop offset="0" stop-color="var(--bubble-top)"/>
            <stop offset="0.5" stop-color="var(--bubble-mid)"/>
            <stop offset="1" stop-color="var(--bubble-top)"/>
          </linearGradient>
        </defs>
        <path d="M51 0 H580 A51 51 0 0 1 631 51 V246 A51 51 0 0 1 580 297 H77 L0 374 V51 A51 51 0 0 1 51 0 Z" fill="url(#bubbleFill)"/>
        <path d="M0 260 V374 L77 297 Z" fill="var(--bubble-tail)" opacity=".55"/>
      </svg>
      <p class="speech__text">Professor Wickersham,<br>how can dogs live<br>longer, healthier lives?</p>
    </div>
  </section>

  <p class="slide-label">Slide - 12</p>
</div>
</body>
</html>
```